Nine Rung Ledger Remedy Seminar

I would like a flyer to hand out to participants at the speeches that we give. We are a CPA firm that specializes in entrepreneurs and realtors. We would like a flyer that looks crisp and clean, that integrates our logo and our company colors (shades of blue & gold). We would like the wording to be as laid out in the attached documents, but design is up to you. We would like a picture to go along with each point and are open to ideas. The flyer should be one page, preferably just the front.

Colors
3176b5
fee18a

Requirements
Must have
• Our logo and the wording supplied.
• A picture to go along with each topic.
Nice to have
• Images that pop, clean look, professional.
Should not have
• Look messy.

```html
<!DOCTYPE html>
<html lang="en">
<head>
<meta charset="utf-8">
<title>Tallyline Figures – Seminar Agenda</title>
<link rel="stylesheet" href="https://fonts.googleapis.com/css2?family=Roboto+Condensed:wght@700&family=Open+Sans:wght@400;600&family=Libre+Baskerville:ital,wght@0,700;1,700&display=swap">
<style>
:root{
  --blue:#3176b5;
  --card-blue:#1a77c0;
  --title-blue:#2a5fa6;
  --navy:#1d2758;
  --gold:#d4aa4a;
  --gold-light:#fee18a;
  --yellow:#f7c324;
  --orange:#ea8a22;
  --white:#ffffff;
  --ink:#1d2758;
}
*{box-sizing:border-box;margin:0;padding:0}
html,body{width:975px;height:1200px;overflow:hidden;background:#fff}
.flyer{position:relative;width:975px;height:1200px;background:var(--white);font-family:"Open Sans",sans-serif}
.header{position:absolute;top:0;left:0;width:975px;height:233px}
.brand{position:absolute;left:0;top:0;width:501px;height:233px;background:var(--white)}
.brand-name{position:absolute;left:55px;top:40px;width:400px;font-family:"Roboto Condensed",sans-serif;font-weight:700;font-size:58px;line-height:62px;color:var(--blue);text-align:center}
.brand-dot{position:absolute;left:232px;top:170px;width:14px;height:14px;border-radius:50%;background:var(--gold)}
.brand-sub{position:absolute;left:0;width:501px;top:196px;text-align:center;font-family:"Libre Baskerville",serif;font-style:italic;font-weight:700;font-size:16px;color:#222}
.welcome{position:absolute;left:501px;top:0;width:474px;height:233px;background:var(--gold)}
.welcome h2{position:absolute;left:24px;top:34px;width:440px;font-family:"Libre Baskerville",serif;font-weight:700;font-size:25px;line-height:35px;color:var(--white)}
.welcome p{position:absolute;left:17px;top:182px;font-size:22px;color:#1a1a1a}
.title-band{position:absolute;top:233px;left:0;width:975px;height:78px;background:var(--title-blue);border-top:6px solid var(--orange)}
.title-band h1{font-family:"Roboto Condensed",sans-serif;font-weight:700;font-size:40px;line-height:70px;color:var(--white);text-align:center;text-shadow:1px 2px 3px rgba(0,0,0,.45)}
.hero{position:absolute;top:311px;left:0;width:975px;height:250px}
.hero-art{position:absolute;top:10px;height:228px}
.hero-art.charts{left:8px;width:380px;background:linear-gradient(160deg,#eaf3fb,#9cc6ea 60%,#e9f1f8)}
.hero-art.money{left:398px;width:570px;background:linear-gradient(110deg,#f3f5f7,#c8d3de 35%,#e3c98e 55%,#6f8b6a 80%,#eef1ec)}
.agenda{position:absolute;top:568px;left:53px;width:876px;display:grid;grid-template-columns:repeat(4,211px);grid-auto-rows:240px;column-gap:11px;row-gap:12px}
.point{position:relative;background:var(--card-blue);border-radius:5px;color:var(--white);font-size:13.6px;line-height:20.2px;padding:10px 10px 0 13px}
.point::first-line{}
.point .num{position:absolute;left:-6px;top:-8px;width:31px;height:31px;border-radius:50%;background:var(--yellow);color:var(--white);font-weight:600;font-size:20px;line-height:31px;text-align:center}
.point .lead{display:inline-block;width:18px}
.point-art{border-radius:0;background:linear-gradient(150deg,#e4f2fb,#a9d3f0 45%,#c7d8b8 70%,#f2ede2)}
.site{position:absolute;top:1064px;left:0;width:975px;text-align:center;font-family:"Roboto Condensed",sans-serif;font-weight:700;font-size:34px;letter-spacing:1.5px;color:var(--ink)}
.footer{position:absolute;top:1108px;left:0;width:975px;height:50px;background:var(--navy)}
.social{position:absolute;left:42px;top:7px;display:flex;gap:10px}
.social span{width:36px;height:36px;border-radius:50%;background:var(--blue)}
.social span:last-child{background:var(--orange)}
.slogan{position:absolute;left:0;top:0;width:975px;height:50px}
.slogan-text{position:absolute;left:300px;top:6px;width:320px;text-align:center;color:var(--white);font-size:15px;line-height:18px}
.phone{position:absolute;right:38px;top:2px;font-family:"Roboto Condensed",sans-serif;font-weight:700;font-size:38px;color:var(--white)}
.cta{position:absolute;top:1158px;left:0;width:975px;height:42px;background:linear-gradient(90deg,var(--yellow),var(--orange));text-align:center;font-size:13.5px;line-height:32px;letter-spacing:.8px;color:#1a1a1a}
</style>
</head>
<body>
<main class="flyer">
  <header class="header">
    <div class="brand">
      <div class="brand-name">Tallyline Figures</div>
      <div class="brand-dot"></div>
      <p class="brand-sub">A Professional Accounting Corporation</p>
    </div>
    <div class="welcome">
      <h2>Welcome to Tallyline Figures Accounting firm licensed in Brookmead, CA.</h2>
      <p>Less Tax. More Fun. Tallyline Figures</p>
    </div>
  </header>

  <div class="title-band"><h1>Nine Rung Ledger Remedy Seminar Agenda:</h1></div>

  <section class="hero">
    <div class="hero-art charts" role="img" aria-label="Glass 3D bar charts and a pie chart resting on financial reports"></div>
    <div class="hero-art money" role="img" aria-label="Calculator, glasses, pen and charts on paperwork beside rising stacks of cash with a red growth arrow"></div>
  </section>

  <section class="agenda">
    <article class="point"><span class="num">1</span><span class="lead"></span>We will first show you how to eliminate much of your self-employment tax on your return by converting your business into an S Corporation. A business owner making over $120,000 per year can save about $12,000 per year by doing this.</article>
    <article class="point"><span class="num">2</span><span class="lead"></span>We will show you how to get tax free income from your corporation by renting you home to the corporation for the board meetings. &nbsp;Many of our clients are getting up to $21,000 in tax free income which could put $8,400 cash into your pocket.</article>
    <article class="point"><span class="num">3</span><span class="lead"></span>We will show you the easiest way to track your expenses so that the only thing you will have to do to have rock solid books is to take a picture of the receipt and throw it away. &nbsp;It doesn’t get any better than that.</article>
    <article class="point"><span class="num">4</span><span class="lead"></span>Next, we show you the importance of tax plan-ning and why it is critical to meet with your CPA before the end of the year and not just when you do your tax prepara-tion.</article>
    <article class="point"><span class="num">5</span><span class="lead"></span>We will show you how to hire your children and get $7,500 per child tax free. &nbsp;This will save you $3,000 per child in income tax reduction.</article>
    <article class="point"><span class="num">6</span><span class="lead"></span>We will discuss how to make your child’s college education tax deductible. &nbsp;With college cost spiraling out of control this is a biggie. &nbsp;Most of our clients have a savings of about $12,000 per year of college.</article>
    <article class="point"><span class="num">7</span><span class="lead"></span>Our grand finale is to show you how to use, not one, but two corpora-tions to get a several hundred thousand dollar tax deferral, get an interest free loan from the government and use that money to grow your business and your wealth.</article>
    <div class="point point-art" role="img" aria-label="Hands using a calculator and pen over cash and tax percentage symbols"></div>
  </section>

  <div class="site">www.tallylinefigurescpa.com</div>

  <footer class="footer">
    <div class="social" aria-label="Social media"><span></span><span></span><span></span><span></span></div>
    <svg class="slogan" width="975" height="50" aria-hidden="true">
      <defs><linearGradient id="arrowFill" x1="0" x2="1"><stop offset="0" stop-color="#2aa4dc"/><stop offset="1" stop-color="#1b5ca8"/></linearGradient></defs>
      <polygon points="300,0 700,0 725,25 700,50 300,50 275,25" fill="url(#arrowFill)"/>
    </svg>
    <div class="slogan-text">GROW YOUR BUSINESS.<br>BUILD A ROCK SOLID TAX PLAN.</div>
    <div class="phone">(555) 014-2290</div>
  </footer>
  <div class="cta">Please call us today and we'll be happy to offer you a free initial consultation.</div>
</main>
</body>
</html>
```